Business card design needed

I need a business card for my new Food & Lifestyle Coaching business - "Bloomvale Food & Lifestlye Coaching"

i already have a logo and would like to have that incorporated into the business card, obviously.

i would like a design that says "fresh" and "funky" - my target market is female, aged 20-45 so i want something that will stand out to them when they see it.

My "Company Colour" is Apple Green
Updates

Thankyou to everyone who has submitted a design for my project. At this stage i have quite a large number of designs to chose from and with only a short time until my project closes i am focusing now on chosing from those i have already shortlisted so am unfortunately not considering any new desings.

Thankyou again for your interest in my project.

Target Market(s)

Female, Health Conscious (or looking to improve their health/lifestyle), aged between 20-45

Industry/Entity Type

Business

Contact Information for Business Card

Tamsin Corley
Ph: 0417382946
Email: eatwell@marovex.com

Requirements
Must have
• Must include my existing Logo
Nice to have
• Would be nice to incoirporate and appointment card on the back

```html
<!DOCTYPE html>
<html lang="en">
<head>
<meta charset="utf-8">
<title>Bloomvale Food &amp; Lifestlye Coaching – Appointment Card</title>
<link rel="stylesheet" href="https://fonts.googleapis.com/css2?family=Cabin:wght@500&display=swap">
<style>
  :root {
    --page: #ffffff;
    --card-rose: #bf6a69;
    --rose-light: rgba(214, 150, 148, 0.55);
    --rose-soft: rgba(214, 150, 148, 0.32);
    --apple-green: #8dc63f;
    --ink: #231f20;
  }
  html, body {
    margin: 0;
    padding: 0;
    width: 1200px;
    height: 702px;
    overflow: hidden;
    background: var(--page);
  }
  .canvas {
    position: relative;
    width: 1200px;
    height: 702px;
  }
  .card {
    position: absolute;
    left: 21px;
    top: 22px;
    width: 1158px;
    height: 663px;
    background: var(--card-rose);
    overflow: hidden;
  }
  .backdrop-glow {
    position: absolute;
    inset: 0;
    background:
      radial-gradient(ellipse 230px 260px at 520px 200px, var(--rose-light), transparent 75%),
      radial-gradient(ellipse 260px 220px at 170px 360px, var(--rose-light), transparent 75%),
      radial-gradient(ellipse 210px 130px at 600px 470px, var(--rose-soft), transparent 75%),
      radial-gradient(ellipse 150px 200px at 330px 600px, var(--rose-soft), transparent 75%);
  }
  .brand-mark {
    position: absolute;
    left: 520px;
    top: 55px;
    width: 120px;
    height: 120px;
    border-radius: 50%;
    background: var(--apple-green);
  }
  .brand-name {
    position: absolute;
    right: 12px;
    top: 10px;
    margin: 0;
    font-family: "Cabin", sans-serif;
    font-weight: 500;
    color: var(--ink);
    text-align: right;
  }
  .brand-title {
    display: block;
    font-size: 98px;
    line-height: 1.2;
  }
  .brand-tagline {
    display: block;
    margin-top: 38px;
    font-size: 29px;
    line-height: 1.2;
  }
  .appointment-lines {
    position: absolute;
    left: 87px;
    top: 0;
    width: 986px;
    height: 100%;
    margin: 0;
    padding: 0;
    list-style: none;
  }
  .appointment-line {
    position: absolute;
    left: 0;
    width: 100%;
    height: 5px;
    background: var(--apple-green);
  }
  .appointment-line:nth-child(1) { top: 358px; }
  .appointment-line:nth-child(2) { top: 443px; }
  .appointment-line:nth-child(3) { top: 525px; }
  .appointment-line:nth-child(4) { top: 607px; }
</style>
</head>
<body>
  <main class="canvas">
    <section class="card" aria-label="Appointment card">
      <div class="backdrop-glow" role="img" aria-label="Faint light rose background decoration"></div>
      <div class="brand-mark" aria-hidden="true"></div>
      <h1 class="brand-name">
        <span class="brand-title">Bloomvale</span>
        <span class="brand-tagline">Food &amp; Lifestlye Coaching</span>
      </h1>
      <ul class="appointment-lines" aria-label="Appointment details">
        <li class="appointment-line"></li>
        <li class="appointment-line"></li>
        <li class="appointment-line"></li>
        <li class="appointment-line"></li>
      </ul>
    </section>
  </main>
</body>
</html>
```